PowerPoint Design Project

We need a powerpoint design for our consulting company, Brindle Consulting. We provide technology strategy and solutioning services, with an emphasis on cloud technology. More information about our services can be found at www.brindleconsulting-example.com

We are looking for a design that is professional, but not corporate stuffy. The design needs to use our primary colors in our brand.
Updates

Reason: We need to iterate on some of the great designs, plus, many people have not had a chance to submit their design yet.

Reason: We had a lot of people accept the project, but not all of them have responded yet. We wanted to get them some time, plus, ask a couple of people to make some minor revisions.

Target Market(s)

Technology buyers between the ages of 30-55 at Vantor 1000 companies

Industry/Entity Type

It Company

Requirements
Must have
• Must follow our logo colors.
Must have at least a cover slide and interior content slide.
Should not have
• Should not contain anything cartoonish or anything with lots of clouds

```html
<!DOCTYPE html>
<html lang="en">
<head>
<meta charset="utf-8">
<title>Brindle Consulting – Slide Templates</title>
<link rel="stylesheet" href="https://fonts.googleapis.com/css2?family=Source+Sans+3:wght@400&display=swap">
<style>
  :root {
    --brand-blue: #1b94c1;
    --brand-brown: #6f645b;
    --divider-grey: #b5b5b5;
    --slide-white: #ffffff;
    --ghost-tint: #e9eef2;
    --ink-dark: #333333;
  }
  * { box-sizing: border-box; margin: 0; padding: 0; }
  html, body { width: 1200px; height: 596px; overflow: hidden; background: var(--slide-white); }
  .deck { position: relative; width: 1200px; height: 596px; font-family: "Source Sans 3", sans-serif; }

  .slide { position: absolute; top: 0; height: 596px; background: var(--slide-white); overflow: hidden; }
  .slide--cover { left: 0; width: 597px; }
  .slide--content { left: 609px; width: 591px; }
  .slide-divider { position: absolute; left: 597px; top: 0; width: 12px; height: 596px; background: var(--divider-grey); }

  .corner-tiles { position: absolute; left: 3px; top: 52px; width: 34px; height: 45px; }
  .corner-tiles span { position: absolute; width: 15px; height: 16px; }
  .tile--blue { background: var(--brand-blue); }
  .tile--brown { background: var(--brand-brown); }

  .side-rule { position: absolute; left: 40px; top: 0; width: 5px; height: 596px; background: var(--brand-brown); }
  .header-rule { position: absolute; left: 40px; right: 0; top: 72px; height: 4px; background: var(--brand-blue); }

  .brand-name {
    position: absolute; left: 62px; top: 14px;
    font-weight: 400; font-size: 38px; line-height: 46px;
    color: var(--brand-brown); white-space: nowrap;
  }

  .cover-backdrop {
    position: absolute; left: 110px; top: 100px; width: 440px; height: 480px;
    background: radial-gradient(ellipse at 50% 45%, var(--ghost-tint) 0%, #f3f5f7 50%, rgba(255,255,255,0) 75%);
  }
  .cover-title {
    position: absolute; left: 45px; right: 0; top: 225px; text-align: center;
    font-weight: 400; font-size: 128px; line-height: 1; letter-spacing: -1px;
    color: var(--brand-brown); white-space: nowrap;
  }

  .placeholder {
    position: absolute; background: var(--brand-blue); color: var(--brand-brown);
    font-weight: 400; display: flex; align-items: center; justify-content: center; white-space: nowrap;
  }
  .placeholder--title { left: 73px; top: 135px; width: 476px; height: 83px; font-size: 46px; }
  .placeholder--subtitle { left: 144px; top: 249px; width: 365px; height: 75px; font-size: 29px; }

  .page-number {
    position: absolute; right: 4px; bottom: 6px;
    font-size: 11px; color: var(--ink-dark);
  }
</style>
</head>
<body>
<main class="deck">

  <section class="slide slide--cover">
    <div class="cover-backdrop" role="img" aria-label="Faint background illustration of laptops connected to a central cloud"></div>
    <div class="corner-tiles">
      <span class="tile--blue" style="left:0;top:0"></span>
      <span class="tile--blue" style="left:18px;top:0"></span>
      <span class="tile--brown" style="left:0;top:29px"></span>
      <span class="tile--brown" style="left:18px;top:29px"></span>
    </div>
    <div class="side-rule"></div>
    <div class="header-rule"></div>
    <div class="brand-name">Brindle Consulting</div>
    <h1 class="cover-title">Title Page</h1>
  </section>

  <div class="slide-divider"></div>

  <section class="slide slide--content">
    <div class="corner-tiles">
      <span class="tile--blue" style="left:0;top:0"></span>
      <span class="tile--blue" style="left:18px;top:0"></span>
      <span class="tile--brown" style="left:0;top:29px"></span>
      <span class="tile--brown" style="left:18px;top:29px"></span>
    </div>
    <div class="side-rule"></div>
    <div class="header-rule"></div>
    <div class="brand-name">Brindle Consulting</div>
    <div class="placeholder placeholder--title">Click to add title</div>
    <div class="placeholder placeholder--subtitle">Click to add subtitle</div>
    <div class="page-number">Page 1</div>
  </section>

</main>
</body>
</html>
```